High value cover design for an A4 ideation pad.

The product is NOT A BOOK.

It's an A4 ideation pad for professionals, designers and creators who handwrite their ideas. Visualise creators like Marcus Tellwind, Owen Prackett and Dale Vorhanek in your mind's eye.

I'm looking for a cover design for the ideation pad. Both front and back.

It should look, feel and convey the following.

--> A handcrafted product experience

--> High value & Elegance

--> Inspiration

Mandatory --> See Uploaded Files --> Files 1, 5 & 6

Target Market(s)

- Designers

-Creative Professionals

- Entrepreneurs

who handwrite their ideas. Visualise creators like Marcus Tellwind, Owen Prackett and Dale Vorhanek in your mind's eye.

Industry/Entity Type

Stationary

Font styles to use
Script
Other font styles liked:
• Calligraphy

Colors
fbed22

Requirements
Must have
• Title text - Amber Lantern

-Text in gold on brown leather background to convey high value for the front cover.

--> High value & Elegance

--> Inspiration

--> Should compel the customers to pick up and own the idea pad
Nice to have
• That's my take but other ideas are welcome
Should not have
• Must not convey

- low value

```html
<!DOCTYPE html>
<html lang="en">
<head>
<meta charset="utf-8">
<title>Amber Lantern — Ideation Pad Cover, Front and Back</title>
<link rel="stylesheet" href="https://fonts.googleapis.com/css2?family=Allura&display=swap">
<style>
  :root {
    --backdrop: #f3f1ec;
    --leather-light: #9a5a3c;
    --leather-mid: #7d4530;
    --leather-deep: #5a2f22;
    --gold: #f2cf3a;
    --gold-line: #d9b52e;
  }
  html, body {
    margin: 0;
    padding: 0;
    width: 1200px;
    height: 839px;
    overflow: hidden;
    background: var(--backdrop);
  }
  .canvas {
    position: relative;
    width: 1200px;
    height: 839px;
  }
  .cover {
    position: absolute;
    top: 95px;
    width: 440px;
    height: 620px;
    box-shadow: 0 2px 6px rgba(0,0,0,0.18);
  }
  .cover--front { left: 82px; }
  .cover--back { left: 669px; }
  .leather {
    position: absolute;
    inset: 0;
    background:
      radial-gradient(ellipse 70% 40% at 50% 18%, rgba(196,128,88,0.45), transparent 70%),
      radial-gradient(ellipse 60% 50% at 35% 80%, rgba(40,18,12,0.35), transparent 70%),
      linear-gradient(180deg, var(--leather-light) 0%, var(--leather-mid) 45%, var(--leather-deep) 100%);
  }
  .title {
    position: absolute;
    margin: 0;
    font-family: "Allura", cursive;
    font-weight: 400;
    color: var(--gold);
    white-space: nowrap;
    line-height: 1;
  }
  .title::after {
    content: "";
    position: absolute;
    left: 0;
    right: 0;
    height: 1px;
    background: var(--gold-line);
  }
  .cover--front .title {
    left: 94px;
    top: 244px;
    width: 243px;
    font-size: 44px;
    text-align: center;
  }
  .cover--front .title::after { bottom: -8px; }
  .cover--back .title {
    left: 141px;
    top: 560px;
    width: 158px;
    font-size: 28px;
    text-align: center;
  }
  .cover--back .title::after { bottom: -5px; }
</style>
</head>
<body>
  <main class="canvas">
    <section class="cover cover--front" aria-label="Front cover">
      <div class="leather" role="img" aria-label="Brown leather texture"></div>
      <h1 class="title">Amber Lantern</h1>
    </section>
    <section class="cover cover--back" aria-label="Back cover">
      <div class="leather" role="img" aria-label="Brown leather texture"></div>
      <p class="title">Amber Lantern</p>
    </section>
  </main>
</body>
</html>
```